Clothes Pop-art web site "Tolmera"

Hello,

its a pop art t-shirt company we appreciate islamic art and arabic heritage
i need a web design that represent my company and offer easy sale platform , i attached some logo sample.

My basic site map will include;
-About
-Tolmera look book
-Tolmera friends- 4 roots
-shop-2 roots Tolmera product-other brand product
-contact-Pixa-Chirpo-KL-Email
-bog via Scrollex

also i attached my busniess card i would like to to have Pixagram-chirpo-kin loop links via the contact root including my email address

My Terms:
-Less SENSELESS SCROLLING
-ALWAYS RESPONSIVE
The general tendency to be entirely responsive across all mobile, tablet and desktop devices. Mobile Friendly Friendly"
Content carousels;
Overly large hero images;
Overused stock photos;
Autoplay videos;
Automated popups;
Advertising sidebars;
“Hello world” blog posts;
Reloading pages;
Modal windows with hidden or tiny close commands;
Loading screens;
Small font sizes;
Long shadows;
Hipster icons and logos.

some website example i like :
http://qv-atelier.example
http://morulatype.example/home
http://gallotrix.example/design/web-illus/illustration-website-design/25/15/pkdalton.example/jpg/s?nid=7206http://gallotrix.example/gallotrix/blog/25-beautiful-and-creative-illustration-themed-web-design-examples

my Main color theme :PANTONE :13-4909 Light Blue

Good Luck

Target Market(s)

teen
youth
unisex

Industry/Entity Type

It Company

Coding

Coded - Design and coding required

Number of Pages Required

3 page

Colors
86cfc6
85cae6
33b8a4
33a6d7
00a990
0792cd

Requirements
Must have
• color theme :PANTONE :13-4909 Light Blue
• arabic calligraphy Ultra modern
• islamic ART patterns ULTRA Modern
Nice to have
• Content carousels;
• Overly large hero images;
• Overused stock photos;
• Autoplay videos;
• Automated popups;
• Advertising sidebars;
• “Hello world” blog posts;
• Reloading pages;
• Modal windows with hidden or tiny close commands;
• Loading screens;
• Small font sizes;
• Long shadows;
• Hipster icons and logos.

```html
<!DOCTYPE html>
<html lang="en">
<head>
<meta charset="utf-8">
<title>Tolmera – Pop Art T-Shirts</title>
<link href="https://fonts.googleapis.com/css2?family=Roboto:wght@300;400;500;700;900&display=swap" rel="stylesheet">
<style>
:root{
  --blue:#33a6d7;
  --blue-deep:#0792cd;
  --teal:#33b8a4;
  --orange:#f7941d;
  --ink:#2b2b2b;
  --grey:#8a8a8a;
  --line:#e2e2e2;
  --paper:#ffffff;
  --mist:#f3f3f3;
  --night:#1d2232;
  --night-2:#262c3f;
}
*{box-sizing:border-box;margin:0;padding:0}
html,body{width:1200px;height:2688px;overflow:hidden}
body{font-family:"Roboto",Arial,sans-serif;color:var(--ink);background:var(--paper);position:relative}
.section{position:absolute;left:0;width:1200px}

/* header */
.site-header{top:0;height:70px;background:var(--paper);border-bottom:1px solid var(--line)}
.brand{position:absolute;left:60px;top:14px;display:flex;align-items:center;gap:10px;font-size:24px;font-weight:700;color:var(--blue)}
.brand-mark{width:36px;height:36px;background:var(--blue);border-radius:4px}
.header-phone{position:absolute;right:190px;top:8px;font-size:12px;color:var(--grey);display:flex;align-items:center;gap:6px}
.main-nav{position:absolute;right:60px;top:38px;display:flex;gap:30px;font-size:13px;color:#444}
.main-nav span.active{color:var(--blue)}

/* hero */
.hero{top:70px;height:770px;background:linear-gradient(180deg,#fafafa,#ececec);overflow:hidden}
.hero-title{position:absolute;top:20px;width:100%;text-align:center;font-size:66px;line-height:1.1;font-weight:500;color:#222;z-index:5}
.hero-sale{position:absolute;top:84px;width:100%;text-align:center;font-size:180px;line-height:1;font-weight:900;color:var(--orange);letter-spacing:4px;z-index:4}
.hero-photo{position:absolute;left:190px;top:230px;width:820px;height:540px;z-index:3;
  background:linear-gradient(180deg,rgba(60,60,70,.15),rgba(40,70,120,.55)),linear-gradient(90deg,#2a2a2a 0 30%,#f2f2f2 30% 68%,#3d7fc2 68%);border-radius:6px 6px 0 0}
.hero-search{position:absolute;right:190px;top:30px;width:34px;height:34px;border-radius:50%;border:2px solid var(--blue);z-index:6}

/* promo strip */
.promo-strip{top:840px;height:170px;background:var(--paper)}
.promo-track{position:absolute;left:210px;top:30px;display:flex;gap:14px}
.promo-tile{width:185px;height:110px;border-radius:3px;position:relative;overflow:hidden;color:#fff;padding:12px;font-size:17px;font-weight:700;line-height:1.1}
.promo-tile .cta{position:absolute;left:12px;bottom:12px;background:var(--orange);font-size:10px;padding:3px 8px;font-weight:500}
.tile-a{background:linear-gradient(90deg,#3a2a1e,#8a5a3a)}
.tile-b{background:linear-gradient(90deg,#222,#7b4a9c)}
.tile-c{background:linear-gradient(90deg,#e9e1d6,#c7a98c)}
.tile-d{background:linear-gradient(90deg,#f4f4f4,#bcbcbc);color:#333}
.arrow{position:absolute;top:70px;font-size:30px;color:#444}

/* video */
.video-block{top:1010px;height:530px;background:var(--paper)}
.video-frame{position:absolute;left:190px;top:0;width:820px;height:500px;background:var(--night-2);overflow:hidden}
.video-title{position:absolute;top:22px;width:100%;text-align:center;color:#fff;font-size:40px;font-weight:400}
.video-sub{position:absolute;top:78px;width:100%;text-align:center;color:#c9c9c9;font-size:12px}
.video-stage{position:absolute;left:60px;top:110px;width:700px;height:340px;background:linear-gradient(135deg,#3a2f28,#5a4a62 50%,#2c3c55)}
.play-btn{position:absolute;left:310px;top:130px;width:80px;height:80px;border-radius:50%;border:4px solid #fff;background:rgba(0,0,0,.35)}
.featured{position:absolute;right:30px;top:40px;background:var(--blue);color:#fff;font-size:13px;padding:8px 12px;width:110px}
.featured small{display:block;font-size:10px;opacity:.85}
.video-controls{position:absolute;left:0;bottom:0;width:100%;height:50px;background:var(--blue);display:flex;justify-content:center;align-items:center;gap:18px;color:#fff;font-size:12px}
.video-controls .bar{width:60px;height:8px;background:#fff;border-radius:4px}

/* products */
.products{top:1540px;height:320px;background:var(--paper)}
.section-title{text-align:center;font-size:30px;color:var(--orange);font-weight:500;padding-top:12px}
.title-rule{width:420px;height:1px;background:var(--line);margin:10px auto 0}
.product-row{position:absolute;left:195px;top:90px;display:flex;gap:10px}
.product-card{width:154px;height:190px;text-align:center;padding-top:8px;background:var(--paper)}
.product-card.is-active{box-shadow:0 2px 10px rgba(0,0,0,.2);height:210px}
.shirt{width:110px;height:110px;margin:0 auto;border-radius:8px}
.product-name{font-size:15px;color:var(--orange);margin-top:8px;font-weight:500}
.product-price{font-size:12px;color:#555;margin-top:4px;display:flex;justify-content:center;gap:8px}
.product-price s{color:#aaa}
.cart-row{font-size:10px;margin-top:8px;display:flex;justify-content:center;gap:6px}
.cart-row .add{background:var(--orange);color:#fff;padding:3px 6px}
.products .arrow{top:180px;color:var(--orange)}

/* social row */
.social-row{top:1860px;height:440px;background:linear-gradient(180deg,#fff,#f5f5f5)}
.blog{position:absolute;left:190px;top:50px;width:240px}
.col-head{font-size:20px;color:var(--orange);font-weight:500;display:flex;justify-content:space-between;align-items:center}
.col-head .tag{font-size:10px;background:var(--blue);color:#fff;padding:2px 6px}
.blog-item{display:flex;gap:10px;margin-top:14px}
.blog-thumb{width:62px;height:54px;background:linear-gradient(135deg,#9bc9e0,#4a7fa6);flex:none}
.blog-item p{font-size:10px;color:#666;line-height:1.35}
.feed-box{position:absolute;left:460px;top:50px;width:290px;height:270px;border:1px solid var(--line);background:#fff;padding:12px}
.feed-top{display:flex;gap:10px;align-items:center}
.feed-logo{width:44px;height:44px;border:1px solid var(--line);display:flex;align-items:center;justify-content:center;color:var(--blue);font-weight:700;font-size:12px}
.feed-top div{font-size:12px;color:#333}
.feed-top small{display:block;color:#999;font-size:10px}
.feed-grid{display:grid;grid-template-columns:repeat(6,1fr);gap:5px;margin-top:16px}
.feed-grid span{height:36px;background:linear-gradient(135deg,#d8d8d8,#9aa7b5)}
.feed-foot{font-size:10px;color:#888;margin-top:12px}
.app-promo{position:absolute;left:780px;top:50px;width:230px}
.app-promo h3{font-size:20px;color:var(--orange);font-weight:500}
.app-promo h4{font-size:11px;color:var(--blue);font-weight:400}
.app-promo ul{list-style:none;font-size:10px;color:#666;margin-top:12px;line-height:1.7;width:120px}
.app-promo ul li::before{content:"✓ ";color:var(--blue)}
.phone-mock{position:absolute;left:140px;top:40px;width:80px;height:170px;border-radius:12px;background:#1e1e1e;padding:14px 6px}
.phone-mock span{display:block;width:100%;height:100%;background:linear-gradient(180deg,#7cc3e4,#2b6d9b)}
.newsletter{position:absolute;right:190px;bottom:30px;width:110px;height:22px;background:var(--orange);color:#fff;font-size:10px;padding:5px 8px}

/* footer */
.site-footer{top:2300px;height:388px;background:var(--night);color:#fff;text-align:center}
.site-footer h2{font-size:34px;font-weight:500;padding-top:34px}
.site-footer .lede{font-size:11px;color:#b5b8c2;margin-top:6px;line-height:1.5}
.pin{margin:18px auto 0;display:block}
.address{font-size:15px;margin-top:6px}
.contact-icons{display:flex;justify-content:center;gap:44px;margin-top:22px}
.contact-item{width:90px;font-size:10px;color:#c9ccd4}
.icon-box{width:60px;height:60px;margin:0 auto 8px;border:3px solid var(--orange);background:var(--blue);display:flex;align-items:center;justify-content:center}
.copyright{position:absolute;bottom:12px;width:100%;font-size:9px;color:#777d8e}
</style>
</head>
<body>

<header class="section site-header">
  <div class="brand"><span class="brand-mark"></span>Tolmera</div>
  <div class="header-phone">
    <svg width="12" height="12" viewBox="0 0 24 24"><path d="M6.6 10.8a15 15 0 006.6 6.6l2.2-2.2a1 1 0 011-.25 11 11 0 003.5.56 1 1 0 011 1V20a1 1 0 01-1 1A17 17 0 013 4a1 1 0 011-1h3.5a1 1 0 011 1 11 11 0 00.56 3.5 1 1 0 01-.25 1z" fill="#33a6d7"/></svg>
    (900)5550147
  </div>
  <nav class="main-nav">
    <span>About</span><span class="active">Tolmera look book</span><span>Tolmera friends</span><span>Brand/Product</span><span>Blog via Scrollex</span><span>Contact</span>
  </nav>
</header>

<section class="section hero">
  <h1 class="hero-title">Hello - Tolmera</h1>
  <div class="hero-sale">SALE</div>
  <div class="hero-search"></div>
  <div class="hero-photo" role="img" aria-label="Three young men modelling printed pop art t-shirts"></div>
</section>

<section class="section promo-strip">
  <span class="arrow" style="left:180px">‹</span>
  <div class="promo-track">
    <div class="promo-tile tile-a" role="img" aria-label="Top brands banner">Top<br>Brands<span class="cta">Shop Now</span></div>
    <div class="promo-tile tile-b" role="img" aria-label="Special t-shirt banner">Special<br>T-Shirt<span class="cta">Shop Now</span></div>
    <div class="promo-tile tile-c" role="img" aria-label="Printed shirt close-up banner"><span class="cta">Shop Now</span></div>
    <div class="promo-tile tile-d" role="img" aria-label="Summer t-shirt banner">Summer T-Shirt<span class="cta">Shop Now</span></div>
  </div>
  <span class="arrow" style="right:180px">›</span>
</section>

<section class="section video-block">
  <div class="video-frame">
    <h2 class="video-title">Play Our Video</h2>
    <p class="video-sub">There are many variations of passages of Lorem Ipsum available</p>
    <div class="video-stage" role="img" aria-label="Video still of a shop wall hung with pop art t-shirts">
      <div class="play-btn"></div>
      <div class="featured">Featured<small>T-Shirt Collection</small></div>
    </div>
    <div class="video-controls">PREV <span class="bar"></span> NEXT</div>
  </div>
</section>

<section class="section products">
  <h2 class="section-title">Our New Products</h2>
  <div class="title-rule"></div>
  <span class="arrow" style="left:175px">‹</span>
  <div class="product-row">
    <div class="product-card"><div class="shirt" style="background:#d9332b" role="img" aria-label="Red printed t-shirt"></div><div class="product-name">New</div><div class="product-price"><span>RM 60.00</span><s>RM 80.00</s></div></div>
    <div class="product-card"><div class="shirt" style="background:#f1f1f1" role="img" aria-label="White printed t-shirt"></div><div class="product-name">New</div><div class="product-price"><span>RM 60.00</span><s>RM 80.00</s></div></div>
    <div class="product-card is-active"><div class="shirt" style="background:linear-gradient(135deg,#f5c542,#8b3fa0)" role="img" aria-label="Colourful pop art t-shirt"></div><div class="product-name">New</div><div class="product-price"><span>RM 60.00</span><s>RM 80.00</s></div><div class="cart-row"><span class="add">Add to cart</span><span>Wishlist</span></div></div>
    <div class="product-card"><div class="shirt" style="background:linear-gradient(135deg,#3ab0e2,#7a4bb5)" role="img" aria-label="Blue graphic t-shirt"></div><div class="product-name">New</div><div class="product-price"><span>RM 60.00</span><s>RM 80.00</s></div></div>
    <div class="product-card"><div class="shirt" style="background:#efefef" role="img" aria-label="White t-shirt with yellow print"></div><div class="product-name">New</div><div class="product-price"><span>RM 60.00</span><s>RM 80.00</s></div></div>
  </div>
  <span class="arrow" style="right:175px">›</span>
</section>

<section class="section social-row">
  <div class="blog">
    <div class="col-head">Blog Posts <span class="tag">View All</span></div>
    <div class="blog-item"><div class="blog-thumb" role="img" aria-label="Blog post thumbnail"></div><p>Fresh prints land this week with bold colour and modern geometric lines.</p></div>
    <div class="blog-item"><div class="blog-thumb" role="img" aria-label="Blog post thumbnail"></div><p>Behind the studio: how each pop art design moves from sketch to shirt.</p></div>
    <div class="blog-item"><div class="blog-thumb" role="img" aria-label="Blog post thumbnail"></div><p>Styling tips for youth streetwear using light blue as your base tone.</p></div>
  </div>

  <div class="feed-box">
    <div class="feed-top"><div class="feed-logo">TM</div><div>Tolmera<small>on kin loop · 1,240 likes</small></div></div>
    <div class="feed-grid">
      <span></span><span></span><span></span><span></span><span></span><span></span>
      <span></span><span></span><span></span><span></span><span></span><span></span>
    </div>
    <p class="feed-foot">kin loop social plugin</p>
  </div>

  <div class="app-promo">
    <h3>Click!</h3>
    <h4>Download now</h4>
    <ul><li>Quick Shopping</li><li>New T-Shirt</li><li>Exclusive Offers</li><li>Order Tracking</li><li>Latest Designs</li><li>Community</li></ul>
    <div class="phone-mock"><span role="img" aria-label="Tolmera mobile app screen"></span></div>
  </div>

  <div class="newsletter">Newsletter ▸</div>
</section>

<footer class="section site-footer">
  <h2>Contact Us</h2>
  <p class="lede">Lorem Ipsum is simply dummy text of the printing<br>and typesetting industry.</p>
  <svg class="pin" width="26" height="34" viewBox="0 0 24 32"><path d="M12 0a11 11 0 00-11 11c0 8 11 21 11 21s11-13 11-21A11 11 0 0012 0z" fill="#fff"/><circle cx="12" cy="11" r="4" fill="#1d2232"/></svg>
  <p class="address">Po Box 41806 Harbor City</p>
  <div class="contact-icons">
    <div class="contact-item"><div class="icon-box"><svg width="26" height="26" viewBox="0 0 24 24"><rect x="6" y="2" width="12" height="20" rx="2" fill="none" stroke="#fff" stroke-width="2"/><circle cx="12" cy="18" r="1.2" fill="#fff"/></svg></div>(900)5550147</div>
    <div class="contact-item"><div class="icon-box"><svg width="28" height="22" viewBox="0 0 28 20"><rect x="1" y="1" width="26" height="18" fill="none" stroke="#fff" stroke-width="2"/><path d="M1 1l13 10L27 1" fill="none" stroke="#fff" stroke-width="2"/></svg></div>hello@tolmera.example</div>
    <div class="contact-item"><div class="icon-box"><svg width="28" height="28" viewBox="0 0 24 24" fill="none" stroke="#fff" stroke-width="1.6"><circle cx="12" cy="12" r="10"/><ellipse cx="12" cy="12" rx="4" ry="10"/><path d="M2 12h20"/></svg></div>www.tolmera.example</div>
    <div class="contact-item"><div class="icon-box"><svg width="22" height="22"><circle cx="11" cy="11" r="9" fill="#fff"/></svg></div>@tolmera_wear</div>
    <div class="contact-item"><div class="icon-box"><svg width="22" height="22"><rect x="2" y="2" width="18" height="18" fill="#fff"/></svg></div>Tolmera_Story</div>
  </div>
  <p class="copyright">© 2015 Tolmera. All rights reserved.</p>
</footer>

</body>
</html>
```